Require stationery design: letter head and update existing business card

clean, simple, minamilistic, los of negative space, black or white. casual, but passionate, informative and knowledgable , no fuss, don to earth.

logo newly created and supplied As AI files in breif. . TO CONFIRM THE FINAL LOGO IS THE VERSION WITH THE GRAPHIC / PICTURE INCLUDED. we now need to update our business card design, take old logo out and replace with new logo, raw business files supplied in brief.
For business card I need proofs with white, black and ligjt timber / rustic cookie.

Target Market(s)

women, house wives, business men, hospitality, higher socio economic, commercial residential, niche market.

Industry/Entity Type

Business

Number of Pages Required

3 page

Font styles to use
Sans Serif

Colors
ffffff
3277b5
0355a3
faa54b
f68e4e

Requirements
Must have
• proofs for business card design to be provided on white, black, timber / cardboard background. logo and business to be supplied in all usable formats and files.
• Letter head to be A4 against white background. Supplier in WORDDOC or send header and footer images as JPEG so I can insert into word template
• suitable quote, invoice, receipt template for emailed pdf's
Nice to have
• stylised touch. finesse. sophistication. we are competed in this kind of market.
• use the colour featured in the screen shot file of a random logo
Should not have
• clutter. be crowded. more than 2 fonts.

```html
<!DOCTYPE html>
<html lang="en">
<head>
<meta charset="utf-8">
<title>Invoice – Timber &amp; Grain Co.</title>
<link href="https://fonts.googleapis.com/css2?family=Lato:ital,wght@0,300;0,400;0,700;0,900;1,400&display=swap" rel="stylesheet">
<style>
:root{
  --backdrop:#d8d8a4;
  --paper:#fcfcf2;
  --olive:#6e6a3b;
  --olive-text:#8a8440;
  --ink:#2b2b2b;
  --muted:#555;
  --grey-col:#c9c9c9;
  --rule:#a9a9a9;
}
*{box-sizing:border-box;margin:0;padding:0}
html,body{width:1200px;height:784px;overflow:hidden}
body{background:var(--backdrop);font-family:'Lato',sans-serif;color:var(--ink);display:flex;align-items:center;justify-content:center}
.sheet{position:relative;width:530px;height:750px;background:var(--paper);box-shadow:0 2px 6px rgba(0,0,0,.12)}

.brand{position:absolute;left:36px;top:34px;display:flex;align-items:center;gap:8px}
.brand-dot{width:12px;height:12px;border-radius:50%;background:var(--olive)}
.brand-name{font-size:15px;font-weight:700;color:var(--ink);letter-spacing:.5px}

.sender{position:absolute;right:36px;top:34px;text-align:right;font-size:8px;line-height:13px;color:var(--ink)}
.sender li{list-style:none;display:flex;align-items:center;justify-content:flex-end;gap:5px}
.sender svg{width:8px;height:8px}

.bill-to{position:absolute;left:36px;top:94px;font-size:8px;line-height:11px}
.bill-to .label{color:var(--olive-text);font-size:9px}
.bill-to .client{font-weight:700;font-size:9px}

.title{position:absolute;left:236px;top:118px;font-size:50px;font-weight:300;letter-spacing:3px;line-height:1}
.title-rule{position:absolute;left:228px;top:104px;width:302px;height:90px}
.meta{position:absolute;left:240px;top:184px;display:flex;gap:40px;font-size:9px;line-height:12px}
.meta strong{display:block;font-size:11px;font-weight:700}

.items{position:absolute;left:36px;top:232px;width:458px;border-collapse:collapse;font-size:9px}
.items th{height:24px;font-size:9px;font-weight:700;letter-spacing:.5px;text-transform:uppercase;text-align:left;padding:0 10px}
.items th.band{background:var(--olive);color:#fff}
.items td{height:44px;padding:0 10px;border-bottom:1px solid var(--rule);vertical-align:middle}
.items td.desc{background:var(--grey-col);width:42%}
.items td.desc b{display:block;font-size:9px}
.items td.desc span{font-size:7.5px;color:var(--muted)}
.items td.num{font-weight:700}

.totals{position:absolute;right:36px;top:506px;width:200px;font-size:10px;font-weight:700}
.totals .line{display:flex;justify-content:space-between;padding:2px 0}
.grand{position:relative;margin-top:8px;height:26px;display:flex;justify-content:space-between;align-items:center;padding:0 12px;color:#fff;font-size:11px;letter-spacing:.5px}
.grand svg{position:absolute;inset:0;width:100%;height:100%;z-index:0}
.grand span{position:relative;z-index:1}

.payment{position:absolute;left:36px;top:512px;font-size:8px;line-height:12px}
.payment h3{font-size:11px;font-weight:700;border-bottom:2px solid var(--olive);display:inline-block;margin-bottom:4px;padding-bottom:1px}

.thanks{position:absolute;left:36px;top:600px;padding-left:10px;border-left:3px solid #c8c8c8;font-size:8px;line-height:12px}
.thanks h2{font-size:13px;font-weight:700;color:var(--olive-text)}
.thanks h4{font-size:8.5px;font-weight:700}

.sign{position:absolute;right:50px;top:638px;text-align:center}
.sign-mark{width:120px;height:30px;background:linear-gradient(90deg,rgba(60,60,60,.08),rgba(60,60,60,.18));margin-bottom:4px}
.sign-name{font-size:11px;font-weight:700}
.sign-role{font-size:8px}
</style>
</head>
<body>
<main class="sheet">
  <div class="brand"><span class="brand-dot"></span><span class="brand-name">Timber &amp; Grain Co.</span></div>

  <ul class="sender">
    <li>123 Street Name Town/City</li>
    <li>State, Country 656</li>
    <li>555 010 274 3186 <svg viewBox="0 0 10 10"><rect width="10" height="10" rx="2" fill="#6e6a3b"/><path d="M3 2.5l1.2 1.6-.6.7a4 4 0 0 0 1.6 1.6l.7-.6 1.6 1.2-.6 1A5 5 0 0 1 2.5 3.1z" fill="#fff"/></svg></li>
    <li>hello@timberandgrain.example <svg viewBox="0 0 10 10"><rect width="10" height="10" rx="2" fill="#6e6a3b"/><path d="M2 3h6v4H2zM2 3l3 2.2L8 3" stroke="#fff" stroke-width=".8" fill="none"/></svg></li>
    <li>www.timberandgrain.example <svg viewBox="0 0 10 10"><circle cx="5" cy="5" r="5" fill="#6e6a3b"/><circle cx="5" cy="5" r="2.6" stroke="#fff" stroke-width=".8" fill="none"/></svg></li>
  </ul>

  <div class="bill-to">
    <div class="label">Invoice to</div>
    <div class="client">NORTHFIELD SYSTEMS LTD</div>
    <div>123 Street name town city/state</div>
    <div>your country 656</div>
    <div>P: +00 555 014 7720</div>
    <div>M: accounts@northfield.example</div>
  </div>

  <svg class="title-rule" viewBox="0 0 302 90" aria-hidden="true"><path d="M0 0h290l12 8v6L292 6H0z" fill="#6e6a3b"/></svg>
  <h1 class="title">INVOICE</h1>
  <div class="meta">
    <div>Total Due:<strong>$ 2500</strong></div>
    <div>Date:<strong>10/June/2018</strong></div>
    <div>Invoice:<strong>#12345</strong></div>
  </div>

  <table class="items">
    <thead><tr><th class="band">Item Description</th><th>Unit Price</th><th class="band">Quantity</th><th class="band">Total</th></tr></thead>
    <tbody>
      <tr><td class="desc"><b>Web Development</b><span>Contrary to popular belief lorem ipsum siply random</span></td><td class="num">$750.00</td><td class="num">2</td><td class="num">$1500.00</td></tr>
      <tr><td class="desc"><b>Web Development</b><span>Contrary to popular belief lorem ipsum siply random</span></td><td class="num">$750.00</td><td class="num">2</td><td class="num">$1500.00</td></tr>
      <tr><td class="desc"><b>Web Development</b><span>Contrary to popular belief lorem ipsum siply random</span></td><td class="num">$750.00</td><td class="num">2</td><td class="num">$1500.00</td></tr>
      <tr><td class="desc"><b>Web Development</b><span>Contrary to popular belief lorem ipsum siply random</span></td><td class="num">$750.00</td><td class="num">2</td><td class="num">$1500.00</td></tr>
      <tr><td class="desc"><b>Web Development</b><span>Contrary to popular belief lorem ipsum siply random</span></td><td class="num">$750.00</td><td class="num">2</td><td class="num">$1500.00</td></tr>
    </tbody>
  </table>

  <div class="totals">
    <div class="line"><span>Sub Total</span><span>$8530.00</span></div>
    <div class="line"><span>Tax Vat 18%</span><span>$120.00</span></div>
    <div class="line"><span>Discount 10%</span><span>$305.00</span></div>
    <div class="grand">
      <svg viewBox="0 0 200 26" preserveAspectRatio="none" aria-hidden="true"><path d="M0 0h200l-8 13 8 13H0z" fill="#6e6a3b"/></svg>
      <span>GRAND TOTAL</span><span>$8530.00</span>
    </div>
  </div>

  <div class="payment">
    <h3>Payment Methods</h3>
    <div>Online: pay@timberandgrain.example</div>
    <div>Payment: Credit Card, Bank Transfer We Accept Cheque</div>
  </div>

  <div class="thanks">
    <h2>Thank you for your business!</h2>
    <h4>Terms &amp; conditions</h4>
    <div>Contrary to popular relief lorem ipsum shit amet it on.</div>
  </div>

  <div class="sign">
    <div class="sign-mark" role="img" aria-label="Handwritten signature of the manager"></div>
    <div class="sign-name">Mark Ellison</div>
    <div class="sign-role">Manager</div>
  </div>
</main>
</body>
</html>
```